velmu GmbH needs great looking businesscards to leave an impression

Dear Designers,

Our company velmu GmbH based in switzerland needs to have impressive businesscards. We produce and sell high quality bleaching products for the upper market.
We'd like to have a minimalistic but still meaningful design. You'll fine our company logo attached and some of our packaging designs. Our company slogan is "discover your smile". If you need additional information feel free to contact us.
Kind Regards Dano

Dear Designers, This is a business card design contest! I try to call the support to fix that. Kind Regards Dano

```html
<!DOCTYPE html>
<html lang="en">
<head>
<meta charset="utf-8">
<title>velmu GmbH – Business Card</title>
<link rel="stylesheet" href="https://fonts.googleapis.com/css2?family=EB+Garamond:wght@400;500&display=swap">
<style>
  :root {
    --backdrop: #4a4a4a;
    --card: #ffffff;
    --rose: #d9837c;
    --mauve: #a87472;
    --teal: #235761;
    --ink: #1c1c1c;
  }
  * { box-sizing: border-box; margin: 0; padding: 0; }
  html, body { width: 1200px; height: 900px; overflow: hidden; }
  body {
    background: var(--backdrop);
    font-family: "EB Garamond", Georgia, serif;
    display: flex;
    flex-direction: column;
    align-items: center;
    justify-content: center;
    gap: 56px;
  }
  .card {
    position: relative;
    width: 640px;
    height: 366px;
    background: var(--card);
    overflow: hidden;
    box-shadow: 0 10px 28px rgba(0,0,0,.35);
  }

  /* decorative colour fields */
  .accent-field { position: absolute; }
  .accent-field--bottom {
    left: 0; right: 0; bottom: 0;
    height: 96px;
    background: linear-gradient(to bottom, var(--rose) 0%, var(--mauve) 30%, var(--teal) 65%);
  }
  .accent-field--side {
    top: 0; right: 0; bottom: 0;
    width: 160px;
    background: linear-gradient(to right, var(--rose) 0%, var(--mauve) 30%, var(--teal) 65%);
  }

  /* front */
  .brand {
    position: absolute;
    left: 92px;
    top: 146px;
    display: flex;
    align-items: center;
    gap: 16px;
  }
  .brand__dot {
    width: 54px; height: 54px;
    border-radius: 50%;
    background: var(--teal);
  }
  .brand__name {
    font-size: 72px;
    font-weight: 500;
    line-height: 1;
    color: var(--teal);
  }

  /* back */
  .contact {
    position: absolute;
    left: 70px;
    top: 42px;
    color: var(--ink);
    font-size: 21px;
    line-height: 1.15;
  }
  .contact__address { font-style: normal; margin-bottom: 22px; }
  .contact__row { display: flex; align-items: center; gap: 10px; }
  .contact__icon { width: 16px; height: 16px; fill: var(--ink); flex: none; }
  .back-brand {
    position: absolute;
    right: 46px;
    bottom: 18px;
    font-size: 40px;
    font-weight: 500;
    line-height: 1;
    color: var(--card);
  }
</style>
</head>
<body>

  <section class="card card--back" aria-label="Business card, contact side">
    <div class="accent-field accent-field--bottom" role="img" aria-label="Decorative colour band in rose, mauve and teal along the bottom edge"></div>
    <div class="contact">
      <address class="contact__address">
        Lukas Ferrand<br>
        Lindenweg 14<br>
        Zürich 8032
      </address>
      <p class="contact__row">
        <svg class="contact__icon" viewBox="0 0 16 16" aria-label="Phone"><path d="M4 1h8a1 1 0 0 1 1 1v12a1 1 0 0 1-1 1H4a1 1 0 0 1-1-1V2a1 1 0 0 1 1-1zm1 2v8h6V3z"/></svg>
        12 12 456 38 0041
      </p>
      <p class="contact__row">
        <svg class="contact__icon" viewBox="0 0 16 16" aria-label="Email"><path d="M1 3h14v10H1zm1.5 1.2L8 8.6l5.5-4.4z"/></svg>
        lukas.ferrand@mailbox.ch
      </p>
    </div>
    <span class="back-brand">velmu</span>
  </section>

  <section class="card card--front" aria-label="Business card, brand side">
    <div class="accent-field accent-field--side" role="img" aria-label="Decorative colour band in rose, mauve and teal along the right edge"></div>
    <div class="brand">
      <span class="brand__name">velmu</span>
      <span class="brand__dot" aria-hidden="true"></span>
    </div>
  </section>

</body>
</html>
```